Buch-/eBook-Cover für Sachbuch gesucht
Zielgruppe
We're selfpublishing nonfiction books. Interested are adults - mostly man (age range: 25-50) - who want to learn more about leadership at their workplaces.
Aufgabenstellung
The design should be clean and simple, title easy to read, good color contrast (the cover has to stand out from an white background).

```html
<!DOCTYPE html>
<html lang="en">
<head>
<meta charset="utf-8">
<title>Leadership – Fostering Growth and Inspiring Excellence</title>
<link rel="stylesheet" href="https://fonts.googleapis.com/css2?family=Archivo+Black&family=Rubik:wght@900&display=swap">
<style>
  :root {
    --navy: #233f80;
    --violet: #7a75a6;
    --lilac: #b3aac8;
    --glow: #f4e6ee;
    --ink-light: #ffffff;
  }
  html, body {
    margin: 0;
    padding: 0;
    width: 847px;
    height: 1200px;
    overflow: hidden;
    background: var(--navy);
  }
  .cover {
    position: relative;
    width: 847px;
    height: 1200px;
    overflow: hidden;
    background: radial-gradient(circle 420px at 51.5% 50%,
      var(--glow) 0%,
      var(--lilac) 22%,
      var(--violet) 48%,
      #3f4f8c 75%,
      var(--navy) 100%);
  }
  .cover__title {
    position: absolute;
    left: 0;
    top: 0;
    width: 847px;
    height: 1200px;
  }
  .cover__title text {
    font-family: "Archivo Black", "Arial Black", sans-serif;
    fill: var(--ink-light);
  }
  .cover__author {
    position: absolute;
    left: 334px;
    top: 58px;
    margin: 0;
    font-family: "Rubik", "Arial Black", sans-serif;
    font-weight: 900;
    font-size: 21px;
    letter-spacing: -0.5px;
    color: var(--ink-light);
    line-height: 1;
  }
  .cover__subtitle {
    position: absolute;
    left: 257px;
    top: 823px;
    margin: 0;
    font-family: "Rubik", "Arial Black", sans-serif;
    font-weight: 900;
    font-size: 60px;
    line-height: 73px;
    letter-spacing: -2.5px;
    color: var(--ink-light);
  }
  .cover__subtitle span { display: block; }
</style>
</head>
<body>
  <main class="cover">
    <svg class="cover__title" viewBox="0 0 847 1200" aria-labelledby="main-title">
      <text id="main-title" transform="translate(199 1173) rotate(-90)"
            font-size="176" textLength="1151" lengthAdjust="spacingAndGlyphs">LEADERSHIP</text>
    </svg>
    <p class="cover__author">Daniel Whitmore</p>
    <h2 class="cover__subtitle">
      <span>Fostering</span>
      <span>Growth</span>
      <span>and</span>
      <span>Inspiring</span>
      <span>Excellence</span>
    </h2>
  </main>
</body>
</html>
```